business card with 2 locations on 1 card

I need a modern looking business card that I would use at 2 different locations. Possibly 1 location on 1 side and other location on other side. One should be able to distinguish the 2 locations immediately before having to read the address or description on card. You can take a look at my website to see what I'm drawn to. The logo is brand new that I just purchased on Craft Hive. I want to emphasize family.
Updates

Let's not use the yellow and blue colors. Added Thursday, August 31, 2017

Target Market(s)

women and children

Industry/Entity Type

Health And Wellness

Contact Information for Business Card

Business name: Willow Brook Chiropractic & Acupuncture
My name: Lorin Daske
Job title: DC, MAOM, LAc (CA), CNS

Location 1
Address: 4817 Marlowe Blvd, Suite B-100, Frisco, TX 75034
Phone: (469) 555-0182
Fax: (972) 555-0137

Location 2
Address: 1936 Belvane Road, Suite 100, Plano, TX 75075
Phone: (469) 555-0169
Fax: (972) 555-0137

Email: drlorindaske@mailnest.example
Website: www.drlorindaske.example

Font styles to use
Serif
Sans Serif

Colors

Designer to choose colors to be used in the design.

Requirements
Must have
• distinction between 2 locations.
Nice to have
• Colors preference below is there. But I like to see what you come up with too!

```html
<!DOCTYPE html>
<html lang="en">
<head>
<meta charset="utf-8">
<title>Willow Brook Chiropractic &amp; Acupuncture – Business Cards</title>
<link rel="stylesheet" href="https://fonts.googleapis.com/css2?family=Cinzel:wght@600&family=Open+Sans:wght@400;700&display=swap">
<style>
  :root {
    --page: #e9ecea;
    --teal: #0e5a63;
    --teal-dark: #0b4c55;
    --green: #138544;
    --green-light: #1a9a52;
    --white: #ffffff;
    --ink: #1d3b3f;
    --title-green: #138544;
  }
  * { box-sizing: border-box; margin: 0; padding: 0; }
  html, body { width: 1200px; height: 874px; overflow: hidden; }
  body {
    background: var(--page);
    font-family: "Open Sans", Arial, sans-serif;
    position: relative;
  }
  .card {
    position: absolute;
    width: 540px;
    height: 300px;
    background: var(--white);
    overflow: hidden;
    box-shadow: 0 3px 10px rgba(0,0,0,.18);
  }
  .card--front-a { left: 40px; top: 96px; }
  .card--back { left: 620px; top: 96px; }
  .card--front-b { left: 330px; top: 480px; }

  /* front */
  .holder { position: absolute; top: 14px; left: 0; width: 100%; text-align: center; color: var(--ink); }
  .holder__name { font-weight: 700; font-size: 17px; line-height: 22px; }
  .holder__title { font-size: 12.5px; line-height: 18px; }
  .card--front-b .holder__title { color: var(--title-green); }

  .location-band { position: absolute; top: 71px; height: 112px; width: 50%; }
  .location-band--frisco { left: 0; background: var(--teal); }
  .location-band--plano { right: 0; background: var(--green); }

  .location {
    position: absolute; top: 22px;
    color: var(--white); font-size: 12.5px; line-height: 17px;
  }
  .location-band--frisco .location { left: 22px; }
  .location-band--plano .location { left: 80px; }
  .location__address { margin-bottom: 8px; }
  .location__line { display: flex; align-items: center; gap: 6px; }
  .location__line svg { width: 11px; height: 11px; fill: var(--white); }

  .emblem {
    position: absolute; left: 213px; top: 70px;
    width: 114px; height: 114px; border-radius: 50%;
    background: var(--white);
    border: 4px solid var(--white);
    box-shadow: inset 0 0 0 3px var(--teal);
  }

  .brand {
    position: absolute; left: 0; width: 100%; top: 194px;
    text-align: center; color: var(--teal);
    font-family: "Cinzel", Georgia, serif; font-weight: 600;
  }
  .brand__name { font-size: 27px; line-height: 30px; letter-spacing: .5px; }
  .brand__tagline { font-size: 11px; line-height: 14px; letter-spacing: .6px; }

  .contact-strip {
    position: absolute; bottom: 0; left: 0; width: 100%; height: 36px;
    display: flex; gap: 3px;
  }
  .contact-strip__item {
    flex: 1; display: flex; align-items: center; justify-content: center; gap: 6px;
    color: var(--white); font-size: 12px;
  }
  .contact-strip__item svg { width: 12px; height: 12px; fill: none; stroke: var(--white); stroke-width: 1.4; }
  .contact-strip__item--email { background: var(--teal); }
  .contact-strip__item--web { background: var(--green); }
  .card--front-b .contact-strip__item--email { background: var(--white); color: var(--ink); }
  .card--front-b .contact-strip__item--email svg { stroke: var(--ink); }

  /* back */
  .card--back {
    background: linear-gradient(135deg, var(--teal-dark) 0%, var(--teal) 45%, var(--green) 100%);
  }
  .world-texture {
    position: absolute; left: 30px; top: 20px; width: 480px; height: 220px;
    background: radial-gradient(ellipse at center, rgba(255,255,255,.10) 0%, rgba(255,255,255,0) 70%);
  }
  .card--back .emblem {
    top: 44px; left: 216px; width: 108px; height: 108px;
    background: transparent; border: 4px solid var(--white); box-shadow: none;
  }
  .card--back .brand { color: var(--white); top: 180px; }
  .back-web {
    position: absolute; top: 262px; left: 0; width: 100%;
    display: flex; align-items: center; justify-content: center; gap: 10px;
    color: var(--white); font-size: 13px; letter-spacing: .3px;
  }
  .back-web__rule { width: 90px; height: 1px; background: rgba(255,255,255,.7); }
</style>
</head>
<body>

<svg width="0" height="0" style="position:absolute">
  <defs>
    <symbol id="icon-phone" viewBox="0 0 24 24"><path d="M6.6 10.8a15 15 0 0 0 6.6 6.6l2.2-2.2a1 1 0 0 1 1-.25 11 11 0 0 0 3.6.6 1 1 0 0 1 1 1V20a1 1 0 0 1-1 1A17 17 0 0 1 3 4a1 1 0 0 1 1-1h3.5a1 1 0 0 1 1 1 11 11 0 0 0 .6 3.6 1 1 0 0 1-.25 1z"/></symbol>
    <symbol id="icon-fax" viewBox="0 0 24 24"><path d="M6 2h10v6H6zM3 9h18v9h-3v4H6v-4H3zm5 7v4h8v-4z"/></symbol>
    <symbol id="icon-mail" viewBox="0 0 24 24"><rect x="2" y="5" width="20" height="14"/><path d="M2 5l10 8 10-8"/></symbol>
    <symbol id="icon-globe" viewBox="0 0 24 24"><circle cx="12" cy="12" r="10"/><path d="M2 12h20M12 2c3 3 3 17 0 20M12 2c-3 3-3 17 0 20"/></symbol>
  </defs>
</svg>

<!-- Front, version A -->
<section class="card card--front-a">
  <div class="holder">
    <p class="holder__name">Lorin Daske,</p>
    <p class="holder__title">DC, MAOM, LAc (CA), CNS</p>
  </div>
  <div class="location-band location-band--frisco">
    <div class="location">
      <p class="location__address">4817 Marlowe Blvd,<br>Suite B-100, Frisco, TX 75034</p>
      <p class="location__line"><svg><use href="#icon-phone"/></svg>(469) 555-0182</p>
      <p class="location__line"><svg><use href="#icon-fax"/></svg>(972) 555-0137</p>
    </div>
  </div>
  <div class="location-band location-band--plano">
    <div class="location">
      <p class="location__address">1936 Belvane Road, Suite 100,<br>Plano, TX 75075</p>
      <p class="location__line"><svg><use href="#icon-phone"/></svg>(469) 555-0169</p>
      <p class="location__line"><svg><use href="#icon-fax"/></svg>(972) 555-0137</p>
    </div>
  </div>
  <div class="emblem"></div>
  <div class="brand">
    <p class="brand__name">WILLOW BROOK</p>
    <p class="brand__tagline">CHIROPRACTIC &amp; ACUPUNCTURE</p>
  </div>
  <div class="contact-strip">
    <p class="contact-strip__item contact-strip__item--email"><svg><use href="#icon-mail"/></svg>drlorindaske@mailnest.example</p>
    <p class="contact-strip__item contact-strip__item--web"><svg><use href="#icon-globe"/></svg>www.drlorindaske.example</p>
  </div>
</section>

<!-- Back -->
<section class="card card--back">
  <div class="world-texture" role="img" aria-label="Faint dotted world map texture"></div>
  <div class="emblem"></div>
  <div class="brand">
    <p class="brand__name">WILLOW BROOK</p>
    <p class="brand__tagline">CHIROPRACTIC &amp; ACUPUNCTURE</p>
  </div>
  <p class="back-web"><span class="back-web__rule"></span>www.drlorindaske.example<span class="back-web__rule"></span></p>
</section>

<!-- Front, version B -->
<section class="card card--front-b">
  <div class="holder">
    <p class="holder__name">Lorin Daske,</p>
    <p class="holder__title">DC, MAOM, LAc (CA), CNS</p>
  </div>
  <div class="location-band location-band--frisco">
    <div class="location">
      <p class="location__address">4817 Marlowe Blvd,<br>Suite B-100, Frisco, TX 75034</p>
      <p class="location__line"><svg><use href="#icon-phone"/></svg>(469) 555-0182</p>
      <p class="location__line"><svg><use href="#icon-fax"/></svg>(972) 555-0137</p>
    </div>
  </div>
  <div class="location-band location-band--plano">
    <div class="location">
      <p class="location__address">1936 Belvane Road, Suite 100,<br>Plano, TX 75075</p>
      <p class="location__line"><svg><use href="#icon-phone"/></svg>(469) 555-0169</p>
      <p class="location__line"><svg><use href="#icon-fax"/></svg>(972) 555-0137</p>
    </div>
  </div>
  <div class="emblem"></div>
  <div class="brand">
    <p class="brand__name">WILLOW BROOK</p>
    <p class="brand__tagline">CHIROPRACTIC &amp; ACUPUNCTURE</p>
  </div>
  <div class="contact-strip">
    <p class="contact-strip__item contact-strip__item--email"><svg><use href="#icon-mail"/></svg>drlorindaske@mailnest.example</p>
    <p class="contact-strip__item contact-strip__item--web"><svg><use href="#icon-globe"/></svg>www.drlorindaske.example</p>
  </div>
</section>

</body>
</html>
```